Investment Company Business Card Design

We need a Business Card design for a new company based in Boston called "Tove Investment". We are cooperating with local real estate and construction companies. Our company is very actively and aggressively acquiring primarily residential investment properties either to buy and hold long term or for purposes or renovating and repositioning for re-sale in the market. In addition, we undertake some development projects and acquisitions as opportunities present themselves. the final design should contains information about “Tove" the river boat. we are tenacious, indomitable, and the business have a favorable wind throughout the voyage for all our investment.
sample Info. on Design:
Lem Durso
CEO
555-xxx-xxxx
418 Perrin St. Suite 507, Boston, MA 02199
Please provide a template also, that we can edit the info later.
Reason: i just got new LOGO Design attached will be use in Business Card Design.
Construction

```html
<!DOCTYPE html>
<html lang="en">
<head>
<meta charset="utf-8">
<title>Tove Investment – Business Card</title>
<link href="https://fonts.googleapis.com/css2?family=Open+Sans:wght@400;600;700&display=swap" rel="stylesheet">
<style>
  :root {
    --stage: #ecebe8;
    --gold: #c9a44a;
    --gold-light: #e4c977;
    --gold-deep: #a88732;
    --card-white: #ffffff;
    --ink: #4a4a4a;
    --ink-soft: #6b6b6b;
    --rule: #d9d9d9;
    --band-grey: #a9a9a9;
  }
  * { box-sizing: border-box; margin: 0; padding: 0; }
  html, body {
    width: 1200px; height: 900px; overflow: hidden;
    background: var(--stage);
    font-family: "Open Sans", Arial, sans-serif;
  }
  .canvas { position: relative; width: 1200px; height: 900px; }

  .card {
    position: absolute; width: 640px; height: 366px;
    border-radius: 4px; overflow: hidden;
    box-shadow: 0 10px 28px rgba(0,0,0,.18);
  }

  /* Back side */
  .card-back {
    left: 90px; top: 60px;
    background: linear-gradient(135deg, var(--gold-deep) 0%, var(--gold) 45%, var(--gold-light) 100%);
  }
  .back-emblem-area {
    position: absolute; left: 180px; top: 20px; width: 380px; height: 320px;
    border-radius: 50%;
    background: radial-gradient(circle, rgba(255,255,255,.22) 0%, rgba(255,255,255,0) 70%);
  }
  .back-name {
    position: absolute; left: 0; right: 0; top: 150px;
    text-align: center; color: #ffffff;
    font-weight: 600; font-size: 50px; letter-spacing: 3px;
    text-transform: uppercase;
  }

  /* Front side */
  .card-front {
    left: 470px; top: 470px;
    background: var(--card-white);
  }
  .front-name-block {
    position: absolute; left: 40px; top: 150px; width: 270px;
    display: flex; align-items: center; gap: 10px;
  }
  .brand-dot { width: 14px; height: 14px; border-radius: 50%; background: var(--gold); flex: none; }
  .brand-name {
    color: var(--gold-deep); font-weight: 600; font-size: 25px;
    letter-spacing: 1px; text-transform: uppercase; white-space: nowrap;
  }
  .divider {
    position: absolute; left: 340px; top: 40px; width: 1px; height: 230px;
    background: var(--rule);
  }
  .details { position: absolute; left: 358px; top: 34px; color: var(--ink); }
  .person-name { color: var(--gold); font-weight: 700; font-size: 22px; line-height: 1.1; }
  .person-title { font-size: 14px; color: var(--ink-soft); margin-top: 2px; }
  .address { font-size: 14px; line-height: 1.35; margin-top: 22px; }
  .contact-list { list-style: none; margin-top: 18px; }
  .contact-list li {
    display: flex; align-items: center; gap: 10px;
    font-size: 15px; line-height: 1.4;
  }
  .contact-list svg { width: 13px; height: 13px; flex: none; }
  .band-line {
    position: absolute; left: 0; right: 0; bottom: 32px; height: 6px;
    background: linear-gradient(90deg, #c8c8c8, var(--band-grey));
  }
  .band-gold {
    position: absolute; left: 0; right: 0; bottom: 0; height: 32px;
    background: linear-gradient(90deg, var(--gold-light), var(--gold) 50%, var(--gold-deep));
  }
</style>
</head>
<body>
<main class="canvas">

  <section class="card card-back" aria-label="Business card back">
    <div class="back-emblem-area" role="img" aria-label="Faint company emblem watermark"></div>
    <div class="back-name">Tove Investment</div>
  </section>

  <section class="card card-front" aria-label="Business card front">
    <div class="front-name-block">
      <span class="brand-dot"></span>
      <span class="brand-name">Tove Investment</span>
    </div>

    <div class="divider"></div>

    <div class="details">
      <p class="person-name">Lem Durso</p>
      <p class="person-title">Managing Member</p>
      <p class="address">418 Perrin St. Suite 507,<br>Boston, MA 02199</p>
      <ul class="contact-list">
        <li>
          <svg viewBox="0 0 16 16" aria-hidden="true"><path fill="var(--gold)" d="M3.5 1.5l2.5 3-1.5 1.8c.8 1.7 2.1 3 3.8 3.8l1.8-1.5 3 2.5-1.3 2.4C6.8 13.2 2.8 9.2 1.2 2.8z"/></svg>
          (555) 361-0196
        </li>
        <li>
          <svg viewBox="0 0 16 16" aria-hidden="true"><rect x="4" y="1" width="8" height="5" fill="var(--gold)"/><rect x="1" y="6" width="14" height="6" rx="1" fill="var(--gold)"/><rect x="4" y="10" width="8" height="5" fill="#fff" stroke="var(--gold)" stroke-width="1.5"/></svg>
          (555) 361-0197
        </li>
        <li>
          <svg viewBox="0 0 16 16" aria-hidden="true"><rect x="4" y="1" width="8" height="14" rx="1.5" fill="none" stroke="var(--gold)" stroke-width="2"/><circle cx="8" cy="12.5" r="1" fill="var(--gold)"/></svg>
          (555) 682-0176
        </li>
        <li>
          <svg viewBox="0 0 16 16" aria-hidden="true"><rect x="1" y="3" width="14" height="10" rx="1" fill="var(--gold)"/><path d="M1.5 3.5L8 9l6.5-5.5" fill="none" stroke="#fff" stroke-width="1.3"/></svg>
          lem@toveinvest.example
        </li>
        <li>
          <svg viewBox="0 0 16 16" aria-hidden="true"><circle cx="8" cy="8" r="7" fill="var(--gold)"/><path d="M1 8h14M8 1c-3 3.5-3 10.5 0 14M8 1c3 3.5 3 10.5 0 14" fill="none" stroke="#fff" stroke-width="1"/></svg>
          www.toveinvest.example
        </li>
      </ul>
    </div>

    <div class="band-line"></div>
    <div class="band-gold"></div>
  </section>

</main>
</body>
</html>
```